Need Business Cards for my Business

email address: rkpmarlowhollowworks@vendrimail.com
web address: rkpmarlowhollowworks.net
Slogan: We offer various QVN licenses
Rowland K. Pemberly
Please stick with colors of Company Logo
would like the card to be more of the color example of the logo.
If you need PDF copy of logo email me at the above account.
Creative control rests with you.

Industry/Entity Type

Business

Contact Information for Business Card

I am a minimalist, but would like something to pop and stand out amongst other cards, make it memorable.

Font styles to use
Serif
Decorative
Script

```html
<!DOCTYPE html>
<html lang="en">
<head>
<meta charset="utf-8">
<title>Marlow Hollow Works – Business Cards</title>
<link href="https://fonts.googleapis.com/css2?family=Open+Sans:wght@400;600&display=swap" rel="stylesheet">
<style>
  :root {
    --bg: #e9e7e3;
    --card: #ffffff;
    --card-shade: #eef0f2;
    --blue: #1f6fb5;
    --navy: #163a63;
    --red: #e0313c;
    --ink: #2b4f7a;
  }
  * { box-sizing: border-box; margin: 0; padding: 0; }
  html, body { width: 1200px; height: 1023px; overflow: hidden; }
  body {
    background: var(--bg);
    font-family: "Open Sans", sans-serif;
    position: relative;
  }
  .card {
    position: absolute;
    left: 320px;
    width: 560px;
    height: 320px;
    border-radius: 14px;
    background: linear-gradient(160deg, var(--card) 40%, var(--card-shade));
    box-shadow: 0 6px 18px rgba(0,0,0,.18);
    overflow: hidden;
  }
  .card--front { top: 120px; }
  .card--back { top: 580px; }

  .wordmark {
    color: var(--blue);
    font-weight: 600;
    font-size: 30px;
    line-height: 1.1;
  }
  .card--front .wordmark {
    position: absolute;
    left: 40px;
    top: 46px;
    display: flex;
    align-items: center;
    gap: 12px;
  }
  .wordmark .dot {
    width: 16px; height: 16px;
    background: var(--red);
    border-radius: 50%;
  }
  .holder {
    position: absolute;
    left: 40px;
    top: 150px;
    color: var(--blue);
    font-weight: 600;
    font-size: 24px;
  }
  .rule {
    position: absolute;
    left: 40px;
    right: 0;
    top: 188px;
    height: 1px;
    background: var(--red);
  }
  .contacts {
    position: absolute;
    left: 44px;
    top: 210px;
    list-style: none;
    color: var(--ink);
    font-size: 13px;
  }
  .contacts li {
    display: flex;
    align-items: center;
    gap: 10px;
    margin-bottom: 9px;
  }
  .contacts svg { width: 13px; height: 13px; flex: none; }

  .card--back .wordmark {
    position: absolute;
    left: 0; right: 0;
    top: 110px;
    text-align: center;
    font-size: 38px;
  }
  .band {
    position: absolute;
    left: 0; right: 0; bottom: 0;
    height: 40px;
    background: var(--navy);
    color: #fff;
    font-size: 13px;
    letter-spacing: .5px;
    display: flex;
    align-items: center;
    padding-left: 40px;
  }
</style>
</head>
<body>
  <section class="card card--front">
    <div class="wordmark"><span class="dot"></span>Marlow Hollow Works</div>
    <p class="holder">Rowland K. Pemberly</p>
    <div class="rule"></div>
    <ul class="contacts">
      <li>
        <svg viewBox="0 0 16 16" aria-hidden="true"><circle cx="8" cy="8" r="7" fill="none" stroke="var(--red)" stroke-width="1.6"/><path d="M5.5 4.5l1.5 1.5-1 1a5 5 0 0 0 3 3l1-1 1.5 1.5-1 1c-3 0-6-3-6-6z" fill="var(--red)"/></svg>
        00-555-01928
      </li>
      <li>
        <svg viewBox="0 0 16 16" aria-hidden="true"><rect x="1" y="3" width="14" height="10" fill="var(--red)"/><path d="M1 3l7 6 7-6" fill="none" stroke="#fff" stroke-width="1.3"/></svg>
        rkpmarlowhollowworks@vendrimail.com
      </li>
      <li>
        <svg viewBox="0 0 16 16" aria-hidden="true"><circle cx="8" cy="8" r="7" fill="var(--red)"/><path d="M1 8h14M8 1c-3 3-3 11 0 14M8 1c3 3 3 11 0 14" fill="none" stroke="#fff" stroke-width="1"/></svg>
        rkpmarlowhollowworks.net
      </li>
    </ul>
  </section>

  <section class="card card--back">
    <div class="wordmark">Marlow Hollow Works</div>
    <div class="band">We offer various QVN licenses</div>
  </section>
</body>
</html>
```